We are growing our coaching practice and need some help creating collateral

Our organisation is building a coaching practice. It's going well and we want to take it to the next level. To date, we've done our own basic marketing material (attached), but now we want to create something more substantial that captures our approach and gives us confidence and pride when talking to customers. Things to note - we aren't looking for logo design, that's a separate branding discussion in our organisation. We are looking for someone to take our existing content and make it look good - this might be in the form of a flyer or PPT slide deck for example.
The format we are looking for is the offering title - in this case, 'Coaching', a brief description, and then some further detail.
Target Market(s)
Corporate, Healthcare, IT
Colors
Designer to choose colors to be used in the design.
Look and feel
Each slider illustrates characteristics of the customer's brand and the style your logo design should communicate.

```html
<!DOCTYPE html>
<html lang="en">
<head>
<meta charset="utf-8">
<title>Executive Coaching</title>
<link href="https://fonts.googleapis.com/css2?family=Arimo:wght@400;700&display=swap" rel="stylesheet">
<style>
  :root {
    --page: #ffffff;
    --panel: #e1e1e1;
    --ink: #111111;
    --brand-ink: #3a3a3a;
    --accent: #e0661f;
    --on-accent: #ffffff;
  }
  * { margin: 0; padding: 0; box-sizing: border-box; }
  html, body {
    width: 1200px;
    height: 675px;
    overflow: hidden;
    background: var(--page);
  }
  .slide {
    position: relative;
    width: 1200px;
    height: 675px;
    background: var(--page);
    font-family: "Arimo", Helvetica, Arial, sans-serif;
  }
  .statement-panel {
    position: absolute;
    left: 22px;
    top: 20px;
    width: 1158px;
    height: 579px;
    background: var(--panel);
  }
  .statement {
    position: absolute;
    left: 151px;
    top: 216px;
    width: 900px;
    font-size: 37px;
    line-height: 45.5px;
    font-weight: 400;
    color: var(--ink);
    letter-spacing: -0.2px;
  }
  .brand-name {
    position: absolute;
    left: 22px;
    top: 630px;
    display: flex;
    align-items: center;
    gap: 8px;
    font-size: 22px;
    font-weight: 400;
    color: var(--brand-ink);
  }
  .brand-dot {
    width: 9px;
    height: 9px;
    border-radius: 50%;
    background: var(--accent);
  }
  .offering-badge {
    position: absolute;
    left: 962px;
    top: 616px;
    width: 238px;
    height: 59px;
  }
  .offering-badge svg { position: absolute; inset: 0; }
  .offering-kicker {
    position: absolute;
    left: 48px;
    top: 8px;
    font-size: 16px;
    font-weight: 400;
    color: var(--on-accent);
    letter-spacing: 0.2px;
  }
  .offering-title {
    position: absolute;
    left: 62px;
    top: 19px;
    font-size: 32px;
    line-height: 1;
    font-weight: 700;
    color: var(--on-accent);
    letter-spacing: 0.3px;
  }
</style>
</head>
<body>
  <main class="slide">
    <section class="statement-panel">
      <p class="statement">We build a creative and confidential partnership with you, one that is grounded in the science of leadership, change and coaching psychology so that practical results are an expectation and not left to chance.</p>
    </section>

    <div class="brand-name">
      <span>Harborline</span>
      <span class="brand-dot"></span>
    </div>

    <div class="offering-badge">
      <svg width="238" height="59" viewBox="0 0 238 59" aria-hidden="true">
        <polygon points="0,0 238,0 238,59 46,59" fill="var(--accent)"/>
      </svg>
      <span class="offering-kicker">EXECUTIVE</span>
      <span class="offering-title">COACHING</span>
    </div>
  </main>
</body>
</html>
```